Marnie Vale Photography needs a unique, creative business card/logo design

I need a design for business cards/logo that is unique and creative in the industry. Simplicity is nice, so not too crowded. Something that will catch my customer's eye and remain in their memory. I am primarily a landscape photographer but will be soon may be branching into boudoir photography as well. I have attached my current card.

Marnie Vale Photography
Phone: 0439 517 264
Email: MarnieValePhotography@quillmail.example
Website: www.snapnook.example/MarnieValePhotography.Aust

Marnie Vale Photography

• Contact Details on one side
• pixelation

```html
<!DOCTYPE html>
<html lang="en">
<head>
<meta charset="utf-8">
<title>Marnie Vale Photography – Business Card</title>
<link href="https://fonts.googleapis.com/css2?family=Raleway:wght@300&family=Open+Sans:wght@400;600&display=swap" rel="stylesheet">
<style>
  :root {
    --backdrop-top: #c9c9c9;
    --backdrop-bottom: #b9b9b9;
    --card-light: #ffffff;
    --card-dark: #2b2b2b;
    --card-dark-edge: #232323;
    --ink-dark: #3a3a3a;
    --ink-body: #4a4a4a;
    --ink-light: #f4f4f4;
  }
  html, body {
    margin: 0;
    width: 1200px;
    height: 900px;
    overflow: hidden;
  }
  body {
    background: linear-gradient(180deg, var(--backdrop-top), var(--backdrop-bottom));
    position: relative;
    font-family: "Open Sans", Arial, sans-serif;
  }
  .card {
    position: absolute;
    top: 306px;
    width: 440px;
    height: 271px;
    border-radius: 12px;
    overflow: hidden;
    box-shadow: 0 1px 3px rgba(0,0,0,0.12);
  }
  .card--contact { left: 149px; background: var(--card-light); }
  .card--brand { left: 608px; }

  .brand-name {
    font-family: "Raleway", Arial, sans-serif;
    font-weight: 300;
    text-align: center;
    margin: 0;
    line-height: 1.1;
  }
  .card--contact .brand-name {
    position: absolute;
    left: 38px;
    top: 48px;
    width: 208px;
    color: var(--ink-dark);
    font-size: 30px;
  }
  .brand-name .brand-sub {
    display: block;
    font-size: 0.45em;
    letter-spacing: 0.12em;
    margin-top: 4px;
  }

  .person-name {
    position: absolute;
    left: 38px;
    top: 138px;
    margin: 0;
    font-weight: 600;
    font-size: 17px;
    color: var(--ink-dark);
  }
  .contact-list {
    position: absolute;
    left: 38px;
    top: 179px;
    margin: 0;
    padding: 0;
    list-style: none;
    font-size: 12px;
    color: var(--ink-body);
  }
  .contact-list li {
    display: flex;
    align-items: center;
    height: 15.5px;
  }
  .contact-icon {
    width: 9px;
    height: 9px;
    margin-right: 10px;
    flex: none;
    fill: var(--ink-dark);
  }

  .brand-backdrop {
    position: absolute;
    inset: 0;
    background: radial-gradient(ellipse at 50% 45%, #333333, var(--card-dark) 55%, var(--card-dark-edge));
  }
  .card--brand .brand-name {
    position: absolute;
    left: 0;
    right: 0;
    top: 96px;
    color: var(--ink-light);
    font-size: 46px;
  }
</style>
</head>
<body>
  <section class="card card--contact">
    <h1 class="brand-name">MARNIE VALE<span class="brand-sub">PHOTOGRAPHY</span></h1>
    <h2 class="person-name">Marnie Vale</h2>
    <ul class="contact-list">
      <li>
        <svg class="contact-icon" viewBox="0 0 10 10" aria-hidden="true"><path d="M2 0.5l1.6 0 0.6 2.2-1 0.8c0.6 1.3 1.5 2.2 2.8 2.8l0.8-1 2.2 0.6 0 1.6c0 0.6-0.5 1-1 1C4 8.5 1.5 6 1 1.5c0-0.5 0.4-1 1-1z"/></svg>
        0439 517 264
      </li>
      <li>
        <svg class="contact-icon" viewBox="0 0 10 10" aria-hidden="true"><path d="M0.5 2h9v6h-9z M1 2.5l4 3 4-3" fill="var(--ink-dark)" stroke="#fff" stroke-width="0.8"/></svg>
        MarnieValePhotography@quillmail.example
      </li>
      <li>
        <svg class="contact-icon" viewBox="0 0 10 10" aria-hidden="true"><rect x="0.5" y="0.5" width="9" height="9" rx="1.5"/></svg>
        snapnook.example/MarnieValePhotography.Aust
      </li>
    </ul>
  </section>

  <section class="card card--brand">
    <div class="brand-backdrop" role="img" aria-label="Dark charcoal background with a faint pattern of overlapping curved strokes"></div>
    <h1 class="brand-name">MARNIE VALE<span class="brand-sub">PHOTOGRAPHY</span></h1>
  </section>
</body>
</html>
```